Bref créative
office materials
pain medicine
Professional
Marlene Dubovski, MD
Anesthesiology and Pain Medicine
4218 Lark Ave, Suite 307
Coral Gables, Florida 33143
novahealclinic@mailvora.com

```html
<!DOCTYPE html>
<html lang="en">
<head>
<meta charset="utf-8">
<title>Novaheal – Business Card</title>
<link rel="stylesheet" href="https://fonts.googleapis.com/css2?family=Arimo:wght@400;700&family=Tinos:wght@400&display=swap">
<style>
  :root {
    --paper: #ffffff;
    --ink: #1a1a1a;
    --brand-green: #5aa83a;
    --motif-green: #dcecd2;
    --motif-green-soft: #eef6e9;
  }
  html, body {
    margin: 0;
    padding: 0;
    width: 1200px;
    height: 686px;
    overflow: hidden;
    background: var(--paper);
  }
  .card {
    position: relative;
    width: 1200px;
    height: 686px;
    background: var(--paper);
    overflow: hidden;
  }
  .backdrop {
    position: absolute;
    left: 660px;
    top: 40px;
    width: 540px;
    height: 646px;
    background:
      radial-gradient(ellipse 60% 55% at 62% 58%, var(--motif-green) 0%, var(--motif-green-soft) 55%, rgba(255,255,255,0) 100%);
  }
  .brand {
    position: absolute;
    left: 48px;
    top: 110px;
    display: flex;
    align-items: center;
    gap: 20px;
  }
  .brand__dot {
    width: 64px;
    height: 64px;
    border-radius: 50%;
    background: var(--brand-green);
    flex: none;
  }
  .brand__name {
    margin: 0;
    font-family: "Arimo", Arial, sans-serif;
    font-weight: 700;
    font-size: 64px;
    line-height: 1;
    color: var(--ink);
  }
  .person {
    position: absolute;
    left: 46px;
    top: 408px;
  }
  .person__name {
    margin: 0;
    font-family: "Arimo", Arial, sans-serif;
    font-weight: 700;
    font-size: 31px;
    color: var(--ink);
  }
  .person__title {
    margin: 6px 0 0;
    font-family: "Arimo", Arial, sans-serif;
    font-size: 25px;
    color: var(--ink);
  }
  .contact {
    position: absolute;
    left: 48px;
    top: 546px;
    font-family: "Tinos", "Times New Roman", serif;
    font-size: 28px;
    line-height: 34px;
    color: var(--ink);
  }
  .contact p { margin: 0; }
  .contact__fax { margin-left: 60px; }
</style>
</head>
<body>
  <main class="card">
    <div class="backdrop" role="img" aria-label="Large faint pale green floral backdrop"></div>

    <header class="brand">
      <span class="brand__dot"></span>
      <h1 class="brand__name">Novaheal</h1>
    </header>

    <section class="person">
      <h2 class="person__name">Marlene Dubovski, MD</h2>
      <p class="person__title">Anesthesiology and Pain Medicine</p>
    </section>

    <section class="contact">
      <p>4218 Lark Ave, Suite 307 Coral Gables, Florida 33143</p>
      <p>Phone : 305-555-0142<span class="contact__fax">Fax : 305-555-0187</span></p>
      <p>Email : novahealclinic@mailvora.com</p>
    </section>
  </main>
</body>
</html>
```